Golf simulator membership club

I need a clean design that associates golf, golfclub, golf simulator. Currently building a golf simulator centre. I need link buttons on top and a short description of the concept on the front page. i have removed the details about booking. Will link to external booking. Maybe also news blog on the right side of the page. Must be responsive to work on PC, iPad, tabs and mobile phone. I have been recommended to ask for WordPress
Industry/Entity Type
Club
Number of Pages Required
1 page
Font styles to use
Sans Serif
Requirements
Must have
- Booking plugin as stated in main description. I have a logo that i have attached.
- Also need a contact form and "meld deg på" form like the one found on my existing homepage brennvik.no

```html
<!DOCTYPE html>
<html lang="no">
<head>
<meta charset="utf-8">
<title>Brennvik.no – Døgnåpen golf simulatorklubb</title>
<link href="https://fonts.googleapis.com/css2?family=Open+Sans:ital,wght@0,400;0,600;0,700;0,800;1,700;1,800&display=swap" rel="stylesheet">
<style>
:root{
  --green:#1f6d37;
  --green-dark:#13502a;
  --green-light:#2f8a47;
  --orange:#f05a28;
  --ink:#333;
  --muted:#777;
  --line:#dcdcdc;
  --panel:#f2f2f2;
  --white:#fff;
}
*{box-sizing:border-box;margin:0;padding:0}
html,body{width:1200px;height:4186px;overflow:hidden}
body{font-family:"Open Sans",Arial,sans-serif;color:var(--ink);background:var(--white);position:relative;font-size:13px;line-height:1.6}
.abs{position:absolute}
p{margin:0}

/* header */
.hero{position:absolute;left:0;top:0;width:1200px;height:545px;background:linear-gradient(180deg,#c9d6d3 0%,#8fa89a 22%,#6d9460 55%,#4f7d41 100%)}
.hero-shade{position:absolute;inset:0;background:linear-gradient(180deg,rgba(255,255,255,.15),rgba(0,0,0,.18))}
.brand{position:absolute;top:36px;left:0;width:1200px;display:flex;justify-content:center;align-items:center;gap:12px}
.brand-dot{width:34px;height:34px;border-radius:50%;background:var(--green)}
.brand-name{font-size:34px;font-weight:700;color:var(--green-dark)}
.mainnav{position:absolute;top:117px;left:0;width:1200px;height:50px;background:var(--green);display:flex;justify-content:center;align-items:center;gap:62px}
.mainnav a{color:#fff;text-decoration:none;font-size:14px;font-weight:600}
.social{position:absolute;left:0;top:190px;width:38px;background:rgba(255,255,255,.85);padding:8px 0;display:flex;flex-direction:column;align-items:center;gap:14px}
.social span{width:16px;height:16px;border-radius:3px;background:#9aa39c}
.booking-tab{position:absolute;left:0;top:418px;width:72px;height:28px;background:var(--orange);color:#fff;font-size:12px;font-weight:700;display:flex;align-items:center;justify-content:center}
.hero-title{position:absolute;top:215px;left:0;width:1200px;text-align:center;color:#fff;font-weight:800;font-style:italic;font-size:36px;text-shadow:0 2px 6px rgba(0,0,0,.45);white-space:nowrap}
.hero-title em{color:var(--orange)}
.hero-sub{position:absolute;top:290px;left:240px;width:860px;color:#fff;font-weight:800;font-style:italic;font-size:31px;line-height:1.3;text-shadow:0 2px 6px rgba(0,0,0,.45);text-align:right;white-space:nowrap}
.hero-sub b{font-size:44px}
.hero-price{position:absolute;top:418px;left:318px;color:#fff;font-style:italic;font-weight:700;font-size:30px;line-height:1.2;text-shadow:0 2px 5px rgba(0,0,0,.4);white-space:nowrap}
.hero-price em{color:var(--orange);font-weight:800}

/* sidebar */
.sidebar{position:absolute;left:795px;top:558px;width:377px;height:1367px;background:var(--panel);padding:30px 14px}
.search{height:34px;background:#fff;border:1px solid var(--line);display:flex;align-items:center;justify-content:space-between;padding:0 12px;color:#aaa;font-size:12px}
.side-h{font-size:14px;font-weight:700;margin:34px 0 14px}
.news{display:flex;gap:14px;margin-bottom:16px}
.news-img{width:86px;height:58px;flex:none;background:linear-gradient(135deg,#8fae7e,#4c7a3e)}
.news h4{font-size:13px;font-weight:600;line-height:1.35}
.news .meta{font-size:11px;color:var(--muted);display:flex;gap:40px;margin-top:6px}
.btn{display:inline-block;background:var(--orange);color:#fff;font-weight:700;font-size:12px;border-radius:16px;padding:6px 22px;text-decoration:none}
.steps p{font-size:12px;line-height:1.6;margin-bottom:16px}
.newsletter{position:absolute;left:14px;top:1046px;width:349px;height:251px;background:#fff;border:4px solid var(--green);text-align:center;padding:24px 26px}
.newsletter h3{font-size:20px;font-weight:600;margin-bottom:8px}
.newsletter p{font-size:11px;color:var(--muted);line-height:1.5}
.newsletter .nl-field{margin:14px 0 12px;height:32px;border:1px solid var(--line);text-align:left;padding:6px 10px;font-size:11px;color:#aaa}

/* content */
.body-text{font-size:12.5px;line-height:1.7;color:#444}
.infobox{position:absolute;left:548px;top:614px;width:232px;text-align:center}
.infobox .mark{width:56px;height:56px;border-radius:50%;background:var(--green);margin:0 auto 10px}
.infobox h3{font-size:21px;font-weight:800;line-height:1.2}
.infobox h3 em{color:var(--orange);font-style:normal}
.infobox p{font-size:15px;font-weight:600;line-height:1.35;margin-top:8px}
.coffee{position:absolute;left:98px;top:893px;width:181px;height:167px;background:radial-gradient(circle at 55% 55%,#e8dccb 0 28%,#4a2c1a 29% 40%,#1d120b 70%)}
.divider{position:absolute;left:0;top:1116px;width:795px;height:14px;background:#f0f0f0}
.accent{position:absolute;left:181px;top:1160px;width:307px;height:8px;background:linear-gradient(90deg,var(--green) 80%,var(--green-dark) 80%)}
.note{position:absolute;left:200px;top:1752px;width:520px;text-align:center;font-size:12px;font-weight:700;line-height:1.5}

/* booking bar */
.bookbar{position:absolute;left:0;top:1892px;width:1200px;height:75px;background:linear-gradient(90deg,var(--green-dark),var(--green-light) 70%);color:#fff}
.bookbar .label{position:absolute;left:98px;top:0;line-height:75px;font-size:19px;font-weight:700}
.step{position:absolute;top:0;height:75px;display:flex;align-items:center;gap:12px;font-size:17px;font-weight:600;white-space:nowrap}
.step i{font-style:normal;width:36px;height:36px;border:2px solid #fff;border-radius:50%;display:flex;align-items:center;justify-content:center;font-size:16px;flex:none}
.step.one{left:240px}
.step.two{left:600px}
.step.last{left:880px;width:320px;background:var(--orange);clip-path:polygon(30px 0,100% 0,100% 100%,30px 100%,0 50%);padding-left:52px}

/* booking form */
.bk-label{position:absolute;left:98px;top:2012px;font-size:13px;font-weight:600}
.select{position:absolute;left:98px;top:2066px;width:64px;height:28px;border:1px solid var(--line);font-size:12px;padding:4px 8px}
.check{position:absolute;left:176px;top:2070px;display:flex;gap:8px;align-items:center;font-size:12px}
.check span{width:14px;height:14px;border:1px solid #999}
.warn{position:absolute;left:98px;top:2136px;display:flex;gap:8px;align-items:center;font-size:11px;color:#888}
.warn span{width:14px;height:14px;border-radius:50%;background:var(--orange)}
.legend{position:absolute;left:98px;top:2212px;display:flex;gap:22px;align-items:center;font-size:12px}
.legend .sq{display:inline-block;width:14px;height:10px;margin-right:6px;vertical-align:middle}
.legend .slot{border:2px solid var(--orange);padding:1px 10px;margin-right:6px;font-style:normal}
.calendar{position:absolute;left:850px;top:2030px;width:300px;height:200px;background:#fff;box-shadow:0 3px 12px rgba(0,0,0,.2);padding:10px 16px;font-size:11px}
.cal-head{display:flex;justify-content:space-between;font-weight:600;margin-bottom:6px}
.cal-grid{display:grid;grid-template-columns:repeat(7,1fr);text-align:center;row-gap:3px;color:#666}
.cal-grid b{font-weight:600;color:#333}
.cal-grid .sel{border:1px solid var(--orange);border-radius:50%;color:var(--orange)}
.cal-grid .off{color:#bbb}

/* simulators */
.sims{position:absolute;left:0;top:2288px;width:1200px;height:670px;background:#f7f7f7;border-top:1px solid var(--line)}
.sim{position:absolute;width:300px;text-align:center}
.sim h3{font-size:18px;font-weight:600}
.sim small{display:block;font-size:11px;color:var(--muted);margin-bottom:18px}
.times{display:grid;grid-template-columns:repeat(4,66px);justify-content:center;row-gap:6px;font-size:12px}
.times i{font-style:normal;height:24px;line-height:20px;border:2px solid transparent}
.times i.b{border-color:var(--orange);font-weight:600}

/* signup */
.signup-band{position:absolute;left:0;top:2972px;width:1200px;height:69px;background:linear-gradient(90deg,var(--green-dark),var(--green-light) 60%,#6fae7c);color:#fff;font-size:20px;font-weight:700;padding:18px 98px}
.signup-intro{position:absolute;left:98px;top:3056px;width:1010px;font-size:11.5px;line-height:1.6;color:#444}
.field{position:absolute;width:380px}
.field label{display:block;font-size:12px;font-weight:600;margin-bottom:6px}
.field label sup{color:var(--orange);font-size:13px}
.field .input{height:34px;border:1px solid var(--line);font-size:11px;color:#aaa;padding:8px 12px}
.field .area{height:92px}
.actions{position:absolute;top:3745px;left:0;width:1200px;display:flex;justify-content:center;gap:20px}
.btn-outline{border:2px solid var(--orange);color:var(--orange);background:#fff;border-radius:16px;padding:5px 24px;font-weight:700;font-size:12px}

/* closing */
.closing{position:absolute;left:0;top:3865px;width:1200px;height:223px;background:linear-gradient(180deg,#8aa995,#5c8750 60%,#466e3b)}
.closing-text{position:absolute;left:0;top:3890px;width:1200px;text-align:center;color:#fff;text-shadow:0 2px 5px rgba(0,0,0,.4)}
.closing-text h2{font-size:32px;font-weight:600;line-height:1.2}
.closing-text p{font-size:18px;margin-top:8px}
.footnav{position:absolute;left:0;top:4088px;width:1200px;height:64px;display:flex;justify-content:center;align-items:center;gap:110px;font-size:13px;font-weight:600}
.copy{position:absolute;left:0;top:4152px;width:1200px;height:34px;background:var(--green);color:#fff;font-size:10px;text-align:center;line-height:34px;letter-spacing:1px}
</style>
</head>
<body>

<header>
  <div class="hero" role="img" aria-label="Golfbane med grønn fairway og fjell i bakgrunnen"><div class="hero-shade"></div></div>
  <div class="brand"><span class="brand-dot"></span><span class="brand-name">Brennvik.no</span></div>
  <nav class="mainnav"><a href="#">startsiden</a><a href="#">nyheter</a><a href="#">kontakt oss</a><a href="#">meld deg på nå</a><a href="#">booking</a></nav>
  <div class="social"><span></span><span></span><span></span><span></span><span></span></div>
  <div class="booking-tab">booking</div>
  <h1 class="hero-title">Døgnåpen <em>golf</em> simulatorklubb</h1>
  <p class="hero-sub">Snart åpner Norges første golfsimulatorklubb<br>på <b>Nøtterøy</b>!</p>
  <p class="hero-price">Kun <em>kr. 750</em>,- per mnd<br>for medlemskap med ubegrenset spilletid.</p>
</header>

<main>
  <p class="abs body-text" style="left:98px;top:572px;width:432px">Vi bygger ut med ny simulator for hvert 15. medlem så her er det førstemann til mølla. Medlemsprisen gir mod tilsvarer noe over 2 timer spill på andre simulatorsenter i Norge.</p>
  <p class="abs body-text" style="left:98px;top:684px;width:432px">Den lave prisen forutsetter at vi har kontinuitet i medlemsmassen og vi har åreforfall på medlemskapet 1. Desember. Dvs at man tegner seg for et år om gangen slik som i golfklubben. (Nye kortere dette oppstartsåret)</p>

  <div class="infobox">
    <div class="mark"></div>
    <h3>Døgnåpen <em>golf</em><br>simulatorklubb</h3>
    <p>FULL HD GRAPHICS<br>+ 6 SIMULATORS<br>+ COFFEE LOUNGE</p>
  </div>

  <div class="coffee" role="img" aria-label="Kopp kaffe med kaffebønner på bordet"></div>
  <p class="abs body-text" style="left:321px;top:890px;width:460px">Vi har en lounge i klubben hvor det blir sofagrupper, kaffemaskin, snacks og mineralvannautomat. Vi vil ha en skjerm med golfkanal i loungeområdet som foresvig er på ca. 50 m2. Vi ønsker å lage en trivelig og aktiv klubb her og det forutsetter at våre medlemmer er aktive og kommer med forbedringsforslag på alle områder etterhvert som vi kommer godt igang. Vi skal jobbe for å få til den gode klubbfølelsen hvor medlemmene kan møtes, spille golf, se på golf i loungen og ha det hyggelig. Dette tror vi kommer til å bli helt topp både i store deler av vinterhalvåret samt på kjølige eller regnfulle dager, sommer etter høstdager. Eller når hjemmebanen har turnering, er fullbooket eller stengt. Husk at vi alle har tilgang til senteret 24/7</p>

  <div class="divider"></div>
  <div class="accent"></div>

  <div class="abs body-text" style="left:98px;top:1196px;width:390px">
    <p style="margin-bottom:14px">Det blir full HD Teeline simulatorer av beste kvalitet og med 120.000 (ja du leste riktig) baner å velge mellom. Lerretet har en størrelse på 4.3 x 3.1m og i full HD kvalitet. Det gir en fantastisk virkelighetsnær presentasjon. Mye grunnet absolutt topp dataøpplast samt HD-1080i prosjektorer av type Short Throw som sitter nærme lerretet og gir en helt utrolig opplevelse. I tillegg slipper man skygge på lerretet (både ved teeshots og putting). Vi har ikke sett alle simulatorer i Norge men ingen av de vi har sett er i nærheten av den samme kvaliteten på bildet som vi får her i klubben.</p>
    <p>Softwaren vi kjører er FSG (Fairway Sim Golf) som sammen med sensorer og kameraet i systemet gir en utrolig nøyaktig analyse av hvert slag og det presenteres på en veldig oversiktlig måte på skjermen rett etter slaget. Du kan hente ut all slags statistikk på deg selv og hvordan du har spilt når du har gått noen runder på simulatoren.</p>
  </div>
  <div class="abs body-text" style="left:530px;top:1150px;width:251px">
    <p style="margin-bottom:14px">I FSG spilles det turneringer hver uke hele året og der kan man melde seg på hvis man ønsker det. Der kan man spille mot andre simulatorgolfere fra hele verden. Turneringene starter som oftest søndag og avsluttes søndag så man har en uke på seg til å spille 4 runder. Under runden din så kan du velge en golfer som har spilt en runde (eks et annet medlem fra dagen før) og du får indikasjon på hvor hans eller hennes ball havnet for hvert slag. Ganske fascinerende og artig. Og det er selvfølgelig gratis.</p>
    <p style="margin-bottom:14px">Se mer info under <span style="color:var(--orange)">Nyheter</span></p>
    <p>Teeline simulatorer har 101 sensorer i utslagsmatten som måler bevegelsen på køllehodet før, ved treffpunktet og ballen samt ballbanen. I tillegg sitter det 2 High speed kameraer som måler ballbanen i hhv horisontalt og vertikalt. En egen innfelt putting sensor matte er plassert en min foran utslagssensoren (også i senter av lerret) og gir en meget nøyaktig måling på putt. Antageligvis den mest virkelighetsnære puttingen mulig på simulator idag.</p>
  </div>

  <p class="note">Vi jobber med den første simulatoren i disse dager og legger ut bilder fortløpende når vi kan den igang. Se info under "nyheter".</p>
  <a class="btn abs" style="left:420px;top:1820px" href="#">Nyheter</a>

  <aside class="sidebar">
    <div class="search"><span>søk nyheter</span>
      <svg width="14" height="14" viewBox="0 0 14 14"><circle cx="6" cy="6" r="4.5" fill="none" stroke="#888" stroke-width="1.5"/><path d="M9.5 9.5l3.5 3.5" stroke="#888" stroke-width="1.5"/></svg></div>
    <h3 class="side-h">Siste nytt</h3>
    <div class="news"><div class="news-img" role="img" aria-label="Bilde av simulatorrommet"></div><div><h4>Se presentasjon av software og hardware</h4><div class="meta"><span>02/27/2017</span><span>10</span></div></div></div>
    <div class="news"><div class="news-img" role="img" aria-label="Bilde av simulatorrommet"></div><div><h4>Se presentasjon av software og hardware</h4><div class="meta"><span>02/27/2017</span><span>10</span></div></div></div>
    <div class="news"><div class="news-img" role="img" aria-label="Bilde av simulatorrommet"></div><div><h4>Se presentasjon av software og hardware</h4><div class="meta"><span>02/27/2017</span><span>10</span></div></div></div>
    <div style="text-align:right;margin-top:8px"><a class="btn" href="#">se alle nyheter</a></div>
    <div style="border-top:1px solid var(--line);margin-top:20px"></div>
    <h3 class="side-h" style="margin-top:16px">Slik er prosessen:</h3>
    <div class="steps">
      <p>1. Meld din interesse her på siden via kontaktskjema, ikke forpliktende!</p>
      <p>2. Vi sender kontrakt på email til deg, du signerer og returnerer til oss.</p>
      <p>3. Du betaler en innmeldingsavgift på 500,- samt første mnd medlemsavgift. Dette skal skje en uke før simulatoren er spilleklar. Dette for å forhindre brukerprofil og kode/ kodebrikke for adgang til senteret.</p>
      <p>3. Du mottar en kode/kodebrikke til senteret og kan starte booking av timer på hvilken som helst ledig simulator i senteret via booking appen og/eller hjemmesiden.</p>
      <p>4. Senteret er åpent 24/7/365 og kun unntaksvis bemannet.</p>
    </div>
    <div style="text-align:right;margin-top:22px"><a class="btn" href="#">kontakt oss</a></div>
    <div class="newsletter">
      <h3>Nyhetsbrev</h3>
      <p>Abonner på vårt nyhetsbrev og få oppdateringer direkte i innboksen din.</p>
      <div class="nl-field">Skriv inn e-post adresse</div>
      <a class="btn" href="#">Abonnere</a>
    </div>
  </aside>

  <section>
    <div class="bookbar">
      <div class="label">BOOKING</div>
      <div class="step one"><i>1</i>Velge antall personer og dato</div>
      <div class="step two"><i>2</i>Velge tid og simulator</div>
      <div class="step last"><i>3</i>Betaling</div>
    </div>

    <div class="bk-label">Antall personer:</div>
    <div class="select">- 1 - ▾</div>
    <div class="check"><span></span>utstilt fra andre medlemmer</div>
    <div class="warn"><span></span>skille fra andre medlemmer vil bli belastet per simulator</div>
    <div class="legend">
      <span><i class="sq" style="background:var(--green)"></i>Reservert eler</span>
      <span><i class="sq" style="background:#ccc"></i>Tomt spor</span>
      <span><i class="slot">09:00</i>tilgjengelig tid</span>
    </div>

    <div class="calendar">
      <div class="cal-head"><span>‹</span><span>februar 2017</span><span>›</span></div>
      <div class="cal-grid">
        <b>Ma</b><b>Ti</b><b>On</b><b>To</b><b>Fr</b><b>Lø</b><b>Sø</b>
        <span class="off">30</span><span class="off">31</span><span>1</span><span>2</span><span>3</span><span>4</span><span>5</span>
        <span>6</span><span>7</span><span>8</span><span>9</span><span>10</span><span>11</span><span>12</span>
        <span>13</span><span>14</span><span>15</span><span>16</span><span>17</span><span>18</span><span>19</span>
        <span>20</span><span>21</span><span class="sel">22</span><span>23</span><span>24</span><span>25</span><span>26</span>
        <span>27</span><span>28</span><span class="off">1</span><span class="off">2</span><span class="off">3</span><span class="off">4</span><span class="off">5</span>
      </div>
    </div>
  </section>

  <section class="sims">
    <div class="sim" style="left:59px;top:30px"><h3>- Simulator 1 -</h3><small>tilgjengelig tid</small><div class="times">
      <i>00:00</i><i>01:00</i><i>02:00</i><i>03:00</i><i>04:00</i><i>05:00</i><i>06:00</i><i>07:00</i><i>08:00</i><i class="b">09:00</i><i class="b">10:00</i><i>11:00</i><i>12:00</i><i class="b">13:00</i><i>14:00</i><i>15:00</i><i>16:00</i><i>17:00</i><i class="b">18:00</i><i>19:00</i><i>20:00</i><i>21:00</i><i class="b">22:00</i><i>23:00</i></div></div>
    <div class="sim" style="left:450px;top:30px"><h3>- Simulator 2 -</h3><small>tilgjengelig tid</small><div class="times">
      <i>00:00</i><i>01:00</i><i>02:00</i><i>03:00</i><i>04:00</i><i>05:00</i><i>06:00</i><i>07:00</i><i>08:00</i><i class="b">09:00</i><i class="b">10:00</i><i>11:00</i><i>12:00</i><i class="b">13:00</i><i>14:00</i><i>15:00</i><i>16:00</i><i>17:00</i><i class="b">18:00</i><i>19:00</i><i>20:00</i><i>21:00</i><i class="b">22:00</i><i>23:00</i></div></div>
    <div class="sim" style="left:827px;top:30px"><h3>- Simulator 3 -</h3><small>tilgjengelig tid</small><div class="times">
      <i>00:00</i><i>01:00</i><i>02:00</i><i>03:00</i><i>04:00</i><i>05:00</i><i>06:00</i><i>07:00</i><i>08:00</i><i class="b">09:00</i><i>10:00</i><i>11:00</i><i>12:00</i><i class="b">13:00</i><i>14:00</i><i>15:00</i><i>16:00</i><i>17:00</i><i class="b">18:00</i><i>19:00</i><i>20:00</i><i>21:00</i><i class="b">22:00</i><i>23:00</i></div></div>
    <div class="sim" style="left:59px;top:360px"><h3>- Simulator 4 -</h3><small>tilgjengelig tid</small><div class="times">
      <i>00:00</i><i>01:00</i><i>02:00</i><i>03:00</i><i>04:00</i><i>05:00</i><i>06:00</i><i>07:00</i><i>08:00</i><i class="b">09:00</i><i class="b">10:00</i><i>11:00</i><i>12:00</i><i class="b">13:00</i><i>14:00</i><i>15:00</i><i>16:00</i><i>17:00</i><i class="b">18:00</i><i>19:00</i><i>20:00</i><i>21:00</i><i class="b">22:00</i><i>23:00</i></div></div>
    <div class="sim" style="left:450px;top:360px"><h3>- Simulator 5 -</h3><small>tilgjengelig tid</small><div class="times">
      <i>00:00</i><i>01:00</i><i>02:00</i><i>03:00</i><i>04:00</i><i>05:00</i><i>06:00</i><i>07:00</i><i>08:00</i><i class="b">09:00</i><i>10:00</i><i>11:00</i><i>12:00</i><i class="b">13:00</i><i>14:00</i><i>15:00</i><i>16:00</i><i>17:00</i><i class="b">18:00</i><i>19:00</i><i>20:00</i><i>21:00</i><i class="b">22:00</i><i>23:00</i></div></div>
    <div class="sim" style="left:827px;top:360px"><h3>- Simulator 6 -</h3><small>tilgjengelig tid</small><div class="times">
      <i>00:00</i><i>01:00</i><i>02:00</i><i>03:00</i><i>04:00</i><i>05:00</i><i>06:00</i><i>07:00</i><i>08:00</i><i class="b">09:00</i><i>10:00</i><i>11:00</i><i>12:00</i><i class="b">13:00</i><i>14:00</i><i>15:00</i><i>16:00</i><i>17:00</i><i class="b">18:00</i><i>19:00</i><i>20:00</i><i>21:00</i><i class="b">22:00</i><i>23:00</i></div></div>
  </section>

  <section>
    <div class="signup-band">meld deg på</div>
    <p class="signup-intro">Bruk skjema for påmelding FØR dere Har mottatt, signert og returnert kontrakten. Vi Bygger en ny simulator drett hver 15. påmeldte Medlem (signert kontrakt). Dere Vil Bli Løpende oppdatert om fremgangen og Estimert Oppstart av "Din" simulator. Betaling en uke av simulator er ferdigstilt.</p>

    <div class="field" style="left:181px;top:3140px"><label>Fornavn : <sup>?</sup></label><div class="input">Skriv inn Fornavn</div></div>
    <div class="field" style="left:697px;top:3140px"><label>Etternavn :</label><div class="input">Skriv inn Fornavn</div></div>
    <div class="field" style="left:181px;top:3224px"><label>Gateadresse :</label><div class="input">Skriv inn Fornavn</div></div>
    <div class="field" style="left:697px;top:3224px"><label>Postnummer :</label><div class="input">Skriv inn Fornavn</div></div>
    <div class="field" style="left:181px;top:3308px"><label>Poststed :</label><div class="input">Skriv inn Fornavn</div></div>
    <div class="field" style="left:697px;top:3308px"><label>Mobilnummer :</label><div class="input">Skriv inn Fornavn</div></div>
    <div class="field" style="left:181px;top:3392px"><label>E-Post : <sup>?</sup></label><div class="input">Skriv inn Fornavn</div></div>
    <div class="field" style="left:697px;top:3392px"><label>Ønsker du tilsendt kontrakt :</label><div class="input" style="width:60px;color:#333">Yes ▾</div></div>
    <div class="field" style="left:181px;top:3476px"><label>Født dd.mm.åååå :</label><div class="input">Skriv inn Fornavn</div></div>
    <div class="field" style="left:697px;top:3476px"><label>Tilsluttet golfklubb (hvis aktuelt) :</label><div class="input">Skriv inn Fornavn</div></div>
    <div class="field" style="left:181px;top:3560px"><label>Kommentar :</label><div class="input area">Skriv inn Fornavn</div></div>

    <div class="actions"><a class="btn" href="#">Send til Brennvik</a><span class="btn-outline">Reset</span></div>
  </section>

  <section>
    <div class="closing" role="img" aria-label="Golfbane i kveldslys som bakgrunn"></div>
    <div class="closing-text">
      <h2>Vi har fått de første påmeldingene. Meld<br>deg på idag for å sikre deg plass.</h2>
      <p>Klikk på lenken "Meld deg på nå" nederst på siden.</p>
    </div>
  </section>
</main>

<footer>
  <nav class="footnav"><span>startsiden</span><span>meld deg på nå</span><span>nyheter</span><span>kontakt oss</span></nav>
  <div class="copy">© 2017 BRENNVIK</div>
</footer>
</body>
</html>
```